Carpal Tunnel - PPC Landing Page

We need to do a SINGLE page landing page for a doctor who specializes in Carpal Tunnel syndrome - please research if you're not familiar - it's very common.

Landing page essentials:
Must have a form in upper right hand corner:
Form title: "Get a free diagnosis."
Form inputs: Name, Phone, Email, Requested Appointment time

Page is for PPC, so needs to be simple and light on content. Content has been provided and attached to this project.

No navigation, just a single page.

Industry/Entity Type

Health

Coding

Coded - Design and coding required

Number of Pages Required

1 page

Requirements
Must have
• Elegant look - Conversion optimized for form and phone
• Responsive design.
Should not have
• Old outdated images.

```html
<!DOCTYPE html>
<html lang="en">
<head>
<meta charset="utf-8">
<title>Carpal Tunnel Specialist – Dr. Kestrel</title>
<link rel="stylesheet" href="https://fonts.googleapis.com/css2?family=Roboto:wght@300;400;500;700&family=Open+Sans:wght@400;600;700&display=swap">
<style>
:root{
  --blue:#1f6fb8;
  --blue-dark:#165a99;
  --red:#d3232f;
  --text:#555a60;
  --heading:#6b6f74;
  --gray-band:#eceeef;
  --card:#ffffff;
  --teal:#1e6873;
  --teal-dark:#174f57;
  --hero-a:#dbe9f3;
  --hero-b:#b9d3e6;
  --line:#d5d9dd;
}
*{box-sizing:border-box;margin:0;padding:0}
html,body{width:678px;height:1200px;overflow:hidden}
body{font-family:"Open Sans",Arial,sans-serif;color:var(--text);background:#f4f5f6;position:relative}

.hero{position:absolute;left:0;top:0;width:678px;height:188px;background:linear-gradient(90deg,var(--hero-a),#eef5fa 55%,var(--hero-b))}
.hero-photo{position:absolute;left:120px;top:0;width:200px;height:188px;background:linear-gradient(180deg,#c6d8e6,#8ea8bd)}
.hero-name{position:absolute;left:322px;top:138px;font-family:"Roboto",sans-serif;font-weight:700;font-size:28px;color:var(--blue)}
.hero-tagline{position:absolute;left:324px;top:170px;font-size:7px;color:var(--text)}

.lead-form{position:absolute;left:497px;top:6px;width:176px;height:94px;background:#fff;padding:6px 10px;box-shadow:0 1px 3px rgba(0,0,0,.15)}
.lead-form h2{font-family:"Roboto",sans-serif;font-weight:700;font-size:12px;color:#3d4247;letter-spacing:.2px;margin-bottom:4px}
.lead-form h2 span{color:var(--red)}
.lead-form .field{height:11px;border:1px solid var(--line);font-size:5.5px;color:#8a8f94;padding:1px 4px;margin-bottom:3px;line-height:8px}
.lead-form .submit{display:block;margin:2px 0 0 auto;width:32px;height:11px;background:var(--red);color:#fff;font-size:5.5px;font-weight:700;text-align:center;line-height:11px;text-transform:uppercase}

.about{position:absolute;left:0;top:188px;width:678px;height:130px;background:#fff;padding:20px 22px}
.about h1{font-family:"Roboto",sans-serif;font-weight:300;font-size:20px;color:var(--heading)}
.about h1 span{color:var(--blue);font-weight:400}
.about-figure{position:absolute;left:22px;top:55px;width:92px;height:58px;background:linear-gradient(135deg,#f1d7c6,#d9a98d)}
.about-text{position:absolute;left:126px;top:55px;width:530px;font-size:7px;line-height:10px}
.about-text p+p{margin-top:6px}

.conditions{position:absolute;left:0;top:318px;width:678px;height:492px;background:var(--gray-band)}
.conditions h2{text-align:center;font-family:"Roboto",sans-serif;font-weight:300;font-size:15px;color:var(--heading);margin-top:14px}
.conditions h2 span{color:var(--blue);font-weight:500}
.card{position:absolute;background:var(--card);padding:8px 10px;font-size:5.6px;line-height:8px}
.card h3{display:flex;align-items:center;gap:6px;font-family:"Roboto",sans-serif;font-size:9px;font-weight:500;color:var(--blue);margin-bottom:5px}
.card h3 i{font-style:normal;width:13px;height:13px;border-radius:50%;background:var(--blue);color:#fff;font-size:7px;display:flex;align-items:center;justify-content:center;flex:none}
.c1{left:22px;top:38px;width:306px;height:98px}
.c2{left:346px;top:38px;width:306px;height:98px}
.c3{left:22px;top:146px;width:306px;height:116px}
.c4{left:346px;top:146px;width:306px;height:116px}
.c5{left:22px;top:272px;width:630px;height:84px}

.contact{position:absolute;left:0;top:810px;width:678px;height:96px;background:var(--teal)}
.contact-map{position:absolute;left:0;top:0;width:370px;height:96px;background:linear-gradient(135deg,#2a7a85,#1c5f69)}
.address{position:absolute;left:385px;top:10px;color:#fff}
.address h2{font-family:"Roboto",sans-serif;font-size:10px;font-weight:700;margin-bottom:5px}
.address ul{list-style:none;font-size:6px;line-height:9px}
.address li{display:flex;gap:5px;align-items:flex-start;margin-bottom:2px}
.address svg{flex:none;margin-top:1px}

.copyright{position:absolute;left:0;top:1182px;width:678px;height:18px;background:var(--teal-dark);color:#cfe0e3;font-size:6px;text-align:center;line-height:18px}
</style>
</head>
<body>

<header class="hero">
  <div class="hero-photo" role="img" aria-label="Portrait photo of the doctor in a suit and tie"></div>
  <div class="hero-name">Dr. Kestrel</div>
  <div class="hero-tagline">Specialist in Carpal Tunnel Syndrome</div>
  <form class="lead-form">
    <h2>GET A <span>FREE</span> DIAGNOSIS</h2>
    <div class="field">Name</div>
    <div class="field">Phone</div>
    <div class="field">Email</div>
    <div class="field">Requested Appointment time</div>
    <span class="submit">Submit</span>
  </form>
</header>

<section class="about">
  <h1>What is <span>Carpal Tunnel Syndrome</span></h1>
  <div class="about-figure" role="img" aria-label="Illustration of a hand showing the carpal tunnel"></div>
  <div class="about-text">
    <p>In Dr. Kestrel's clinical practice, Carpal Tunnel Syndrome is one of the most commonly reported health problems. Carpal tunnel occurs when swelling pinches the median nerve, which provides sensation to the palm side of the thumb, index finger, middle finger and to the inside half of the ring finger.</p>
    <p>The result can be a combination of tingling, numbness, weakness and pain in the fingers, thumb, palm or the forearm. If the condition is not treated, permanent deterioration of muscle tissue can occur.</p>
  </div>
</section>

<section class="conditions">
  <h2>Other conditions treated by <span>Dr. Kestrel:</span></h2>

  <article class="card c1">
    <h3><i>1</i>Cubital Tunnel Syndrome (Cell Phone Elbow)</h3>
    <p>Similar to carpal tunnel syndrome, cubital tunnel syndrome is a condition brought on by increased pressure. This occurs when the ulnar nerve is irritated at the inner elbow. The loss of feeling and tingling in the ring and little fingers is common, often made worse by bending the elbow for long periods such as holding a phone. People who lean on their elbows at work are more likely to develop the problem, and early care can prevent lasting weakness in the hand and grip.</p>
  </article>

  <article class="card c2">
    <h3><i>2</i>DeQuervains Tenosynovitis</h3>
    <p>Also known as thumb tendonitis, this is one of the most common tendon problems seen in the wrist. It is caused by irritation or swelling of the tendons found along the thumb side of the wrist. Pain can be felt when turning the wrist, gripping or making a fist. It often appears after repetitive lifting, such as carrying a baby, and can develop slowly over weeks. Treatment may include splinting, rest and targeted therapy to reduce swelling and restore motion.</p>
  </article>

  <article class="card c3">
    <h3><i>3</i>Dupuytren's Disease</h3>
    <p>Dupuytren's Disease is caused by an abnormal thickening of the palm and fingers. This dense tissue may form small lumps that slowly pull one or more fingers into a bent position. The ring and little fingers are affected most often. The condition is not usually painful, but it can make it hard to lay the hand flat, shake hands or wear gloves. It occurs more often in men over fifty and may run in families. Your doctor will check how far the fingers bend and discuss whether gentle release or other care is right for you. Early review helps keep the hand working well for daily tasks.</p>
  </article>

  <article class="card c4">
    <h3><i>4</i>Hand Sprains</h3>
    <p>Sprains result from forcing a joint to move beyond its normal range of motion. Finger sprains occur when the ligaments holding the joint together are stretched or torn. These injuries are common in sports and falls and can cause swelling, pain and stiffness in the fingers and thumb. A mild sprain may heal with rest, ice and support, while a severe sprain can lead to an unstable joint if left untreated. An exam and imaging help decide the right splint or treatment, and gentle exercises later restore strength and movement so you can return to normal use.</p>
  </article>

  <article class="card c5">
    <h3><i>5</i>Hand Fractures</h3>
    <p>Fractures of the fingers occur when a finger is hit, crushed or bent too far, and they are among the most common injuries of the hand. Breaks may happen in the small bones of the fingers or in the long bones of the palm. Signs include pain, swelling, bruising and difficulty moving the finger, and in some cases the finger may look crooked. Proper alignment is important so the hand keeps its strength and shape. Many fractures heal well with a splint or cast, while others need a small procedure to hold the bones in place. Prompt care gives the best chance of a full recovery and a hand that works as it should.</p>
  </article>
</section>

<section class="contact">
  <div class="contact-map" role="img" aria-label="Street map showing the clinic location"></div>
  <div class="address">
    <h2>CORPORATE ADDRESS:</h2>
    <ul>
      <li><svg width="7" height="9" viewBox="0 0 7 9"><path d="M3.5 0a3 3 0 0 0-3 3c0 2.3 3 6 3 6s3-3.7 3-6a3 3 0 0 0-3-3zm0 4.2a1.2 1.2 0 1 1 0-2.4 1.2 1.2 0 0 1 0 2.4z" fill="#fff"/></svg><span>118 Birchwood Avenue, Suite 4<br>Lakeview Medical Plaza<br>Springvale, ST 40218</span></li>
      <li><svg width="7" height="7" viewBox="0 0 7 7"><path d="M1.4 0l1.2 1.7-.7.9a4 4 0 0 0 2.5 2.5l.9-.7L7 5.6 6 7C2.8 6.6.4 4.2 0 1z" fill="#fff"/></svg><span>(555) 014-2290, 014-2291</span></li>
    </ul>
  </div>
</section>

<footer class="copyright">© 2024 Dr. Kestrel. All Rights Reserved.</footer>

</body>
</html>
```